Architectural Hardware Package Design

We need some new packaging for our stainless steel wire balustrade products. The packaging will include our logo (see in files) and will be consistent with the colours in our our style guide (also included). The packaging in to be modern and high quality. We will also include some text and a QR code to go inside the packaging. The main function of the box is to protect the product. For the most part the design on the outside can be pretty plain and more vibrant inside for when it is opened. The product can be heavy so the packaging needs to be durable. I have included an example of some KX4 packaging which I think would be a good basis for the design (Note we won't have an inert going into the box..

The Box Dimensions are to be as below. The box will needs flaps etc. so it can be folded together.
W: 380mm x L: 380mm x H: 200mm

```html
<!DOCTYPE html>
<html lang="en">
<head>
<meta charset="utf-8">
<title>Tellex Solutions – Balustrade Mailer Box Dieline</title>
<link href="https://fonts.googleapis.com/css2?family=Montserrat:wght@600&display=swap" rel="stylesheet">
<style>
  :root {
    --paper: #ffffff;
    --steel-dark: #6d8196;
    --steel-mid: #9fb0c0;
    --steel-light: #e6ecf1;
    --dieline: #d9782d;
    --ink: #1c1c1c;
  }
  html, body {
    margin: 0;
    padding: 0;
    width: 1200px;
    height: 1200px;
    overflow: hidden;
    background: var(--paper);
  }
  .artboard {
    display: block;
    width: 1200px;
    height: 1200px;
  }
  .cut-line {
    fill: none;
    stroke: var(--dieline);
    stroke-width: 1.6;
  }
  .company-name, .tagline {
    font-family: "Montserrat", sans-serif;
    font-weight: 600;
    fill: var(--ink);
    text-anchor: middle;
  }
  .company-name { letter-spacing: 0.5px; }
  .tagline { letter-spacing: 0.5px; }
</style>
</head>
<body>
<svg class="artboard" viewBox="0 0 1932 1932" xmlns="http://www.w3.org/2000/svg">
  <defs>
    <linearGradient id="steel-sheen" x1="0" y1="0.2" x2="1" y2="0">
      <stop offset="0" stop-color="var(--steel-mid)"/>
      <stop offset="0.1" stop-color="var(--steel-light)"/>
      <stop offset="0.22" stop-color="var(--steel-mid)"/>
      <stop offset="0.33" stop-color="var(--steel-light)"/>
      <stop offset="0.45" stop-color="var(--steel-mid)"/>
      <stop offset="0.55" stop-color="var(--steel-light)"/>
      <stop offset="0.68" stop-color="var(--steel-mid)"/>
      <stop offset="0.78" stop-color="var(--steel-light)"/>
      <stop offset="1" stop-color="var(--steel-dark)"/>
    </linearGradient>
  </defs>

  <rect class="steel-surface" x="88" y="64" width="1778" height="1780" fill="url(#steel-sheen)"
        role="img" aria-label="Brushed stainless steel texture covering the box surface"/>

  <g class="dieline">
    <rect class="cut-line" x="734" y="90" width="478" height="257"/>
    <path class="cut-line" d="M733 90 C600 90 500 200 503 320 L505 350 L733 352"/>
    <path class="cut-line" d="M1212 92 C1340 95 1435 200 1431 300 L1431 340 L1212 342"/>
    <rect class="cut-line" x="734" y="347" width="478" height="477"/>
    <path class="cut-line" d="M733 352 L498 428 L498 745 L733 823"/>
    <path class="cut-line" d="M1212 345 L1446 425 L1446 750 L1212 820"/>
    <rect class="cut-line" x="734" y="824" width="478" height="259"/>
    <rect class="cut-line" x="535" y="824" width="199" height="256"/>
    <rect class="cut-line" x="1212" y="822" width="188" height="253"/>
    <rect class="cut-line" x="734" y="1083" width="478" height="477"/>
    <rect class="cut-line" x="478" y="1080" width="256" height="482"/>
    <rect class="cut-line" x="214" y="1085" width="264" height="475"/>
    <rect class="cut-line" x="1212" y="1075" width="256" height="495"/>
    <rect class="cut-line" x="1468" y="1074" width="256" height="494"/>
    <rect class="cut-line" x="734" y="1560" width="478" height="250"/>
    <rect class="cut-line" x="540" y="1565" width="193" height="247"/>
    <rect class="cut-line" x="1213" y="1570" width="186" height="240"/>
  </g>

  <g class="lid-branding">
    <text class="company-name" x="952" y="540" font-size="24">Tellex Solutions</text>
    <text class="tagline" x="952" y="570" font-size="12">STAINLESS STEEL WIRE</text>
    <text class="tagline" x="952" y="584" font-size="12">BALUSTRADE PRODUCTS</text>
  </g>

  <g class="wall-branding">
    <text class="company-name back-mark" x="969" y="955" font-size="15">Tellex Solutions</text>
    <text class="company-name front-mark" x="968" y="1683" font-size="15">Tellex Solutions</text>
    <text class="company-name left-side-mark" transform="translate(612 1320) rotate(-90)" font-size="15">Tellex Solutions</text>
    <text class="company-name right-side-mark" transform="translate(1322 1315) rotate(90)" font-size="15">Tellex Solutions</text>
  </g>
</svg>
</body>
</html>
```